BUSINESS CARD DESIGN

NAME- TODD MASVERIK
PHONE NUMER - 808- 451-7082
EMAIL- OFFICE@VORLINDE-GRADEWAY.COM
BACK OF CARD- SPEACIALIZES IN LAND CLEARING, FORESTRY MUCLHING AND EXCAVATION

Contact Information for Business Card

NAME- TODD MASVERIK PHONE NUMER - 808- 451-7082 EMAIL- OFFICE@VORLINDE-GRADEWAY.COM BACK OF CARD- SPEACIALIZES IN LAND CLEARING , MUCLHING AND EXCAVATION

```html
<!DOCTYPE html>
<html lang="en">
<head>
<meta charset="utf-8">
<title>Vorlinde Gradeway business card</title>
<link href="https://fonts.googleapis.com/css2?family=Montserrat:wght@600;700;800&display=swap" rel="stylesheet">
<style>
  :root {
    --ink: #000000;
    --paper: #ffffff;
    --gold: #f7b218;
    --page: #ffffff;
  }
  * { margin: 0; padding: 0; box-sizing: border-box; }
  html, body { width: 1200px; height: 1132px; overflow: hidden; background: var(--page); }
  body { position: relative; font-family: "Montserrat", sans-serif; color: var(--gold); }

  .card { position: absolute; left: 255px; width: 690px; height: 394px; overflow: hidden; }
  .card--front { top: 151px; background: var(--paper); }
  .card--back { top: 626px; background: var(--ink); }

  .front-wave { position: absolute; inset: 0; }

  .brand { position: absolute; display: flex; flex-direction: column; align-items: center; text-align: center; }
  .brand__mark { border-radius: 50%; border: 4px solid var(--gold); }
  .brand__name { font-weight: 800; letter-spacing: 0.06em; line-height: 1.15; }
  .brand__sub { font-weight: 700; letter-spacing: 0.45em; }

  .card--front .brand { left: 24px; width: 250px; top: 100px; }
  .card--front .brand__mark { width: 110px; height: 110px; margin-bottom: 14px; }
  .card--front .brand__name { font-size: 17px; }
  .card--front .brand__sub { font-size: 9px; margin-top: 6px; }

  .card--back .brand { left: 195px; width: 300px; top: 70px; }
  .card--back .brand__mark { width: 150px; height: 150px; margin-bottom: 18px; }
  .card--back .brand__name { font-size: 24px; }
  .card--back .brand__sub { font-size: 11px; margin-top: 8px; }

  .person { position: absolute; left: 373px; top: 104px; }
  .person__name { font-size: 29px; font-weight: 800; line-height: 1; letter-spacing: 0.01em; }
  .person__role { display: inline-block; font-size: 20px; font-weight: 700; margin-top: 6px; padding-right: 12px; padding-bottom: 2px; border-bottom: 3px solid var(--ink); }

  .contacts { position: absolute; left: 373px; top: 225px; list-style: none; }
  .contacts__item { display: flex; align-items: center; height: 24px; margin-bottom: 17px; font-size: 13px; font-weight: 700; }
  .contacts__icon { width: 26px; height: 24px; margin-right: 17px; flex: none; }

  .tagline { position: absolute; left: 0; right: 0; top: 341px; text-align: center; font-size: 12.5px; font-weight: 700; letter-spacing: 0.06em; }
</style>
</head>
<body>

<section class="card card--front">
  <svg class="front-wave" viewBox="0 0 690 394" width="690" height="394" aria-hidden="true">
    <path d="M0 0 H345 V233 C345 300 260 345 177 338 C150 336 140 326 100 330 C50 336 20 365 0 394 Z" fill="var(--ink)"/>
  </svg>

  <div class="brand">
    <div class="brand__mark"></div>
    <div class="brand__name">VORLINDE GRADEWAY</div>
    <div class="brand__sub">LLC · HAWAII</div>
    <div class="brand__sub">808-451-7082</div>
  </div>

  <div class="person">
    <h1 class="person__name">TODD MASVERIK</h1>
    <p class="person__role">OWNER</p>
  </div>

  <ul class="contacts">
    <li class="contacts__item">
      <svg class="contacts__icon" viewBox="0 0 26 24" aria-hidden="true">
        <rect x="1" y="5" width="24" height="15" fill="var(--ink)"/>
        <path d="M2 6 L13 14 L24 6 M2 19 L10 12 M24 19 L16 12" stroke="var(--paper)" stroke-width="1.6" fill="none"/>
      </svg>
      OFFICE@VORLINDE-GRADEWAY.COM
    </li>
    <li class="contacts__item">
      <svg class="contacts__icon" viewBox="0 0 26 24" aria-hidden="true">
        <path d="M6 2 L9 2 L11 7 L8 9 C9 13 12 16 16 17 L18 14 L23 16 L23 20 C23 22 21 23 19 23 C10 22 3 15 2 6 C2 4 4 2 6 2 Z" fill="none" stroke="var(--ink)" stroke-width="1.5"/>
        <path d="M15 3 C19 4 21 6 22 10 M15 7 C17 7.5 18 8.5 18.5 10.5" fill="none" stroke="var(--ink)" stroke-width="1.5"/>
      </svg>
      +808- 451-7082
    </li>
    <li class="contacts__item">
      <svg class="contacts__icon" viewBox="0 0 26 24" aria-hidden="true">
        <g fill="none" stroke="var(--ink)" stroke-width="1.5">
          <circle cx="13" cy="12" r="10.5"/>
          <ellipse cx="13" cy="12" rx="4.5" ry="10.5"/>
          <path d="M2.5 12 H23.5 M4 6.5 H22 M4 17.5 H22 M13 1.5 V22.5"/>
        </g>
      </svg>
      WWW.VORLINDE-GRADEWAY.COM
    </li>
  </ul>
</section>

<section class="card card--back">
  <div class="brand">
    <div class="brand__mark"></div>
    <div class="brand__name">VORLINDE GRADEWAY</div>
    <div class="brand__sub">LLC · HAWAII</div>
    <div class="brand__sub">808-451-7082</div>
  </div>
  <p class="tagline">SPEACIALIZES IN LAND CLEARING , MUCLHING AND EXCAVATION</p>
</section>

</body>
</html>
```